3 x 3 metre trade booth design

We need a design for a 3 x 3 metre corner booth for a conference we are attending. There will therefore be 2 x backdrops that we need to have designed. For one of them we want to have our services displayed as an engaging, modern infographic. For the other, we would like to have our brand tagline and our logo, with a cool background which aligns with what we do.
I have attached a picture of what our booth looked like last year- we designed this ourself and we need it to look much more professional, with a different type of infographic for the
Please see attachment with full design brief attached

```html
<!DOCTYPE html>
<html lang="en">
<head>
<meta charset="utf-8">
<title>Vantora – Booth Backdrops</title>
<link rel="stylesheet" href="https://fonts.googleapis.com/css2?family=Archivo:wght@300;400;500;600;700;800&display=swap">
<style>
  :root{
    --backdrop:#888888;
    --panel:#fbfafc;
    --ink:#16131a;
    --purple:#8b4aa3;
    --gold:#f5d93f;
    --amber:#e8b83a;
    --divider:#ececf0;
  }
  html,body{margin:0;padding:0;width:1200px;height:1200px;overflow:hidden;background:var(--backdrop);}
  .booth{display:block;width:1200px;height:1200px;font-family:"Archivo",sans-serif;}
  .tagline-light{font-weight:300;fill:#fff;font-size:64px;}
  .tagline-bold{font-weight:700;fill:#fff;font-size:49px;}
  .brand-name{font-weight:800;fill:var(--ink);font-size:40px;letter-spacing:5px;}
  .web{font-weight:400;fill:var(--ink);font-size:28px;}
  .kicker{font-weight:500;fill:var(--amber);font-size:14px;letter-spacing:3.5px;}
  .title-main{font-weight:800;fill:var(--purple);font-size:74px;}
  .title-sub{font-weight:800;fill:var(--ink);font-size:42px;letter-spacing:.5px;}
  .step-num{font-weight:600;fill:#fff;font-size:17px;}
  .service-head{font-weight:700;fill:var(--ink);font-size:16px;}
  .service-item{font-weight:400;fill:var(--ink);font-size:16px;}
  .bullet{fill:var(--gold);}
  .route{fill:none;stroke:var(--purple);stroke-width:2;}
</style>
</head>
<body>
<svg class="booth" viewBox="0 0 1932 1932" xmlns="http://www.w3.org/2000/svg">
  <defs>
    <linearGradient id="warmGrad" x1="0" y1="0" x2="1" y2="1">
      <stop offset="0" stop-color="#a577a8"/>
      <stop offset="0.5" stop-color="#d9ad6a"/>
      <stop offset="0.85" stop-color="#f5d93f"/>
    </linearGradient>
    <linearGradient id="ringGrad" x1="0" y1="1" x2="1" y2="0">
      <stop offset="0" stop-color="#9a5aa5"/>
      <stop offset="1" stop-color="#f3e6b8" stop-opacity="0.5"/>
    </linearGradient>
    <linearGradient id="violetGrad" x1="0" y1="0" x2="0" y2="1">
      <stop offset="0" stop-color="#9574ab"/>
      <stop offset="1" stop-color="#8a52a0"/>
    </linearGradient>
    <linearGradient id="dotGrad" x1="0" y1="0" x2="1" y2="1">
      <stop offset="0" stop-color="#a36fb0"/>
      <stop offset="1" stop-color="#f5d93f"/>
    </linearGradient>
    <linearGradient id="arrowGrad" x1="1" y1="1" x2="0" y2="0">
      <stop offset="0" stop-color="#a566b4"/>
      <stop offset="1" stop-color="#f5e2a0" stop-opacity="0.3"/>
    </linearGradient>
  </defs>

  <!-- Backdrop panels -->
  <rect x="95" y="530" width="1742" height="871" fill="var(--panel)"/>
  <line x1="966" y1="530" x2="966" y2="1401" stroke="var(--divider)" stroke-width="1.5"/>

  <!-- Left backdrop: brand & tagline -->
  <g class="brand-panel">
    <circle cx="392" cy="930" r="312" fill="none" stroke="url(#ringGrad)" stroke-width="3"/>
    <circle cx="392" cy="930" r="257" fill="url(#warmGrad)"/>
    <circle cx="727" cy="1121" r="220" fill="none" stroke="var(--purple)" stroke-width="2.5"/>
    <circle cx="727" cy="1121" r="203" fill="url(#violetGrad)"/>

    <text class="tagline-light" x="378" y="937" text-anchor="middle">Transforming</text>
    <text class="tagline-light" x="378" y="999" text-anchor="middle">Brands into</text>
    <text class="tagline-bold" x="731" y="1088" text-anchor="middle">Nimbus</text>
    <text class="tagline-bold" x="729" y="1137" text-anchor="middle">Success</text>
    <text class="tagline-bold" x="729" y="1187" text-anchor="middle">Stories</text>

    <rect x="556" y="610" width="60" height="60" fill="var(--amber)"/>
    <text class="brand-name" x="660" y="656">VANTORA</text>

    <text class="web" x="155" y="1351">www.vantora.com</text>
  </g>

  <!-- Right backdrop: service infographic -->
  <g class="service-panel">
    <rect x="1284" y="606" width="236" height="28" rx="14" fill="none" stroke="var(--amber)" stroke-width="1.5"/>
    <text class="kicker" x="1402" y="625" text-anchor="middle">OUR SERVICE MODEL</text>
    <text class="title-main" x="1401" y="701" text-anchor="middle">FULL SERVICE</text>
    <text class="title-sub" x="1401" y="751" text-anchor="middle">MANAGEMENT</text>

    <!-- Corner arrows -->
    <path d="M1800 574 L1742 628 M1742 588 V628 H1804" fill="none" stroke="url(#arrowGrad)" stroke-width="9"/>
    <path d="M1002 1366 L1058 1312 M998 1308 H1063 V1368" fill="none" stroke="url(#dotGrad)" stroke-width="9" opacity="0.85"/>

    <!-- Route line -->
    <path class="route" d="M727 900 V872 Q727 833 767 833 H1030 M1088 833 H1282 M1340 833 H1578 M1634 833 H1697 A124 124 0 0 1 1697 1081 H1158 A117 117 0 0 0 1138 1311 M1196 1315 H1446 M1504 1315 H1837"/>

    <g class="steps">
      <circle cx="1059" cy="833" r="27" fill="#fff"/><circle cx="1059" cy="833" r="23" fill="url(#dotGrad)"/>
      <text class="step-num" x="1059" y="839" text-anchor="middle">1</text>
      <circle cx="1311" cy="833" r="27" fill="#fff"/><circle cx="1311" cy="833" r="23" fill="url(#dotGrad)"/>
      <text class="step-num" x="1311" y="839" text-anchor="middle">2</text>
      <circle cx="1605" cy="833" r="27" fill="#fff"/><circle cx="1605" cy="833" r="23" fill="url(#dotGrad)"/>
      <text class="step-num" x="1605" y="839" text-anchor="middle">3</text>
      <circle cx="1165" cy="1315" r="27" fill="#fff"/><circle cx="1165" cy="1315" r="23" fill="url(#dotGrad)"/>
      <text class="step-num" x="1165" y="1321" text-anchor="middle">4</text>
      <circle cx="1474" cy="1315" r="27" fill="#fff"/><circle cx="1474" cy="1315" r="23" fill="url(#dotGrad)"/>
      <text class="step-num" x="1474" y="1321" text-anchor="middle">5</text>
    </g>

    <g class="service" transform="translate(1035 0)">
      <text class="service-head" x="0" y="894">Nimbus Account Setup</text>
      <path class="bullet" d="M0 917 l6 4 l-6 4z"/><text class="service-item" x="12" y="927">Cost analysis to scale</text>
      <text class="service-item" x="12" y="947">profitably</text>
      <path class="bullet" d="M0 961 l6 4 l-6 4z"/><text class="service-item" x="12" y="971">Nimbus account setup</text>
      <path class="bullet" d="M0 985 l6 4 l-6 4z"/><text class="service-item" x="12" y="995">Account audit</text>
      <path class="bullet" d="M0 1009 l6 4 l-6 4z"/><text class="service-item" x="12" y="1019">Nimbus Brand Registry</text>
    </g>

    <g class="service" transform="translate(1287 0)">
      <text class="service-head" x="0" y="894">Account Management</text>
      <path class="bullet" d="M0 917 l6 4 l-6 4z"/><text class="service-item" x="12" y="927">Catalogue management</text>
      <path class="bullet" d="M0 941 l6 4 l-6 4z"/><text class="service-item" x="12" y="951">Account health monitoring</text>
      <path class="bullet" d="M0 965 l6 4 l-6 4z"/><text class="service-item" x="12" y="975">Case log &amp; issue resolution</text>
      <path class="bullet" d="M0 989 l6 4 l-6 4z"/><text class="service-item" x="12" y="999">Stock &amp; Fulfilment Management</text>
      <path class="bullet" d="M0 1013 l6 4 l-6 4z"/><text class="service-item" x="12" y="1023">Customised Reporting</text>
    </g>

    <g class="service" transform="translate(1582 0)">
      <text class="service-head" x="0" y="894">Nimbus Advertising</text>
      <path class="bullet" d="M0 917 l6 4 l-6 4z"/><text class="service-item" x="12" y="927">Sponsored Ads (PPC)</text>
      <path class="bullet" d="M0 941 l6 4 l-6 4z"/><text class="service-item" x="12" y="951">Bid automation</text>
      <path class="bullet" d="M0 965 l6 4 l-6 4z"/><text class="service-item" x="12" y="975">Demand-Side Platform</text>
      <text class="service-item" x="12" y="995">(DSP)</text>
    </g>

    <g class="service" transform="translate(1141 0)">
      <text class="service-head" x="0" y="1153">International Expansion</text>
      <path class="bullet" d="M0 1175 l6 4 l-6 4z"/><text class="service-item" x="12" y="1185">Market opportunity analysis</text>
      <path class="bullet" d="M0 1199 l6 4 l-6 4z"/><text class="service-item" x="12" y="1209">Launch in new marketplaces</text>
      <path class="bullet" d="M0 1223 l6 4 l-6 4z"/><text class="service-item" x="12" y="1233">Listing localisation</text>
      <path class="bullet" d="M0 1247 l6 4 l-6 4z"/><text class="service-item" x="12" y="1257">Logistics &amp; Fulfilment strategy</text>
    </g>

    <g class="service" transform="translate(1451 0)">
      <text class="service-head" x="0" y="1153">Brand Content &amp; Optimisation</text>
      <path class="bullet" d="M0 1175 l6 4 l-6 4z"/><text class="service-item" x="12" y="1185">Rich Media / Enhanced Brand Content</text>
      <path class="bullet" d="M0 1199 l6 4 l-6 4z"/><text class="service-item" x="12" y="1209">Brand store</text>
      <path class="bullet" d="M0 1223 l6 4 l-6 4z"/><text class="service-item" x="12" y="1233">Product listing optimisation</text>
      <path class="bullet" d="M0 1247 l6 4 l-6 4z"/><text class="service-item" x="12" y="1257">Search Engine Optimisation (SEO)</text>
    </g>
  </g>
</svg>
</body>
</html>
```